Fennick Executive Search - New Business Card Design Project

We are an executive search firm called Fennick Executive Search based in the UK. We require a custom design for a business card. We're looking to convey a professional service to executives for executive search recruitment services. In terms of colours, we like dark blues and grays (maybe even silver incorporated somewhere if we go for a foiled type of card) but we're open to your artistic flare. See our current logo in attachments. We are totally open on design so long as the design is slick and professional.
Updates

Thanks for all your contributions of various designs. I have to say the quality of work has been amazing which is going to make our job quite difficult in the coming days on making a decision. Thanks to you all that have taken the time to submit designs thus far. We'll keep on reviewing and try to narrow down our selection as soon as possible.

Target Market(s)

Executive Search

Industry/Entity Type

Recruitment

Contact Information for Business Card

Fennick Executive Search,
Exclusively Sourcing & Hiring Senior Leaders
Gordon Pellbury, Managing Director,
07823 906417
0117 486 7132
gordon@fennickexecutive.co.uk
fennickexecutive.co.uk
58 Lindmoor Court, Hatherley Road, Bristol, BS32 9QJ

Font styles to use
Sans Serif
Other font styles liked:
• Roboto (which is used in our logo)

Requirements
Must have
• Our logo (It has a subtle fade on it from #02071d at top to #333649 at bottom)
• The logo can be on one side or both sides
• Must be elegant and professional
• We have 2nd slogan ADVISE | ENGAGE | EVOLVE | ACHIEVE which can be incorporated into the card
Nice to have
• Use of blues and grey colours
• Compatible with similar styling to our website fennickexecutive.co.uk
Should not have
• Must not be overly brash
• Must not contain cartoon characters

```html
<!DOCTYPE html>
<html lang="en">
<head>
<meta charset="utf-8">
<title>Fennick Executive Search – Business Card</title>
<link rel="stylesheet" href="https://fonts.googleapis.com/css2?family=Roboto:wght@400;500;700&display=swap">
<style>
  :root {
    --navy-top: #0f1627;
    --navy-bottom: #2f3447;
    --ink: #111522;
    --paper: #ffffff;
    --backdrop: #e6e7eb;
    --on-dark: #ffffff;
  }
  * { margin: 0; padding: 0; box-sizing: border-box; }
  html, body { width: 1200px; height: 1000px; overflow: hidden; }
  body {
    background: var(--backdrop);
    font-family: "Roboto", Arial, sans-serif;
    position: relative;
  }
  .card {
    position: absolute;
    width: 493px;
    height: 318px;
  }
  .card--back {
    left: 489px; top: 453px;
    background: var(--paper);
    color: var(--ink);
  }
  .card--front {
    left: 175px; top: 231px;
    background: linear-gradient(to bottom, var(--navy-top), var(--navy-bottom));
    color: var(--on-dark);
    z-index: 2;
  }
  .brand {
    position: absolute;
    left: 90px; top: 91px;
    color: var(--on-dark);
    line-height: 1;
    white-space: nowrap;
  }
  .brand__line1 { display: block; font-size: 68px; font-weight: 700; }
  .brand__line2 { display: block; font-size: 34px; font-weight: 500; margin-top: -3px; }
  .front-rule {
    position: absolute;
    left: 62px; top: 267px;
    width: 368px; height: 2px;
    background: var(--on-dark);
  }
  .slogan {
    position: absolute;
    left: 0; right: 0; top: 283px;
    text-align: center;
    font-size: 15.5px;
    font-weight: 500;
    letter-spacing: 0.4px;
    white-space: nowrap;
  }
  .spine {
    position: absolute;
    left: 230px; top: 39px;
    width: 3px; height: 239px;
    background: var(--ink);
  }
  .icon {
    position: absolute;
    left: 212px;
    width: 39px; height: 39px;
  }
  .icon--phone { top: 87px; }
  .icon--pin { top: 190px; }
  .person {
    position: absolute;
    right: 290px; top: 139px;
    text-align: right;
    white-space: nowrap;
  }
  .person__name { font-size: 18.5px; font-weight: 700; line-height: 22px; }
  .person__role { font-size: 15px; font-weight: 500; line-height: 20px; }
  .contact {
    position: absolute;
    left: 263px;
    font-size: 13.5px;
    line-height: 17px;
    white-space: nowrap;
  }
  .contact--phone { top: 90px; }
  .contact--web { top: 142px; }
  .contact--address { top: 198px; left: 266px; }
</style>
</head>
<body>
  <section class="card card--back" aria-label="Business card back">
    <div class="spine"></div>
    <svg class="icon icon--phone" viewBox="0 0 40 40" aria-hidden="true">
      <circle cx="20" cy="20" r="19.5" fill="#111522"/>
      <path d="M14.5 11.5c.8-.6 1.9-.4 2.4.5l1.6 2.9c.4.8.2 1.7-.5 2.2l-1.2.9c.9 2.3 2.4 4.2 4.3 5.6l1.1-.9c.7-.5 1.6-.5 2.2.1l2.5 2.3c.7.7.7 1.8 0 2.5l-1.4 1.3c-1 .9-2.5 1.1-3.7.4-4.500-2.6-7.6-6.6-8.6-11.5-.3-1.4.2-2.9 1.3-3.8z" fill="#ffffff"/>
    </svg>
    <svg class="icon icon--pin" viewBox="0 0 40 40" aria-hidden="true">
      <circle cx="20" cy="20" r="19.5" fill="#111522"/>
      <path d="M20 9.5c-4.3 0-7.5 3.2-7.5 7.3 0 5.3 7.5 13.7 7.5 13.7s7.5-8.4 7.5-13.7c0-4.1-3.2-7.3-7.5-7.3z" fill="#ffffff"/>
      <circle cx="20" cy="17" r="3" fill="#111522"/>
    </svg>
    <div class="person">
      <p class="person__name">Gordon Pellbury</p>
      <p class="person__role">Managing Director</p>
    </div>
    <p class="contact contact--phone">07823 906417<br>0117 486 7132</p>
    <p class="contact contact--web">gordon@fennickexecutive.co.uk<br>www.fennickexecutive.co.uk</p>
    <p class="contact contact--address">58 Lindmoor Court, Hatherley Road<br>Bristol, BS32 9QJ</p>
  </section>

  <section class="card card--front" aria-label="Business card front">
    <p class="brand">
      <span class="brand__line1">FENNICK</span>
      <span class="brand__line2">EXECUTIVE SEARCH</span>
    </p>
    <div class="front-rule"></div>
    <p class="slogan">ADVISE | ENGAGE | EVOLVE | ACHIEVE</p>
  </section>
</body>
</html>
```